Criação de Layout para Website para Engenharia e Construção Civil
" Empresa de projetos e serviços de construção Civil que atua no seguimento de licitações publicas, obras e reformas particulares, avaliações e pericias, gerenciamento de contratos, orçamentos, planejamento. Sou Engenheiro Civil e devido à demanda no seguimento de projetos tenho três engenheiros que trabalham na empresa sob-regime de prestação de serviços, ou seja, sem vinculo direto (nesse caso parecido com o sistema Quadrimba e seus desainer´s). "

```html
<!DOCTYPE html>
<html lang="pt-BR">
<head>
<meta charset="utf-8">
<title>Estrutor – Engenharia & Construção Civil</title>
<link href="https://fonts.googleapis.com/css2?family=Open+Sans:ital,wght@0,400;0,600;0,700;0,800;1,600;1,700&display=swap" rel="stylesheet">
<style>
:root{
  --green:#3c9a3f;
  --green-dark:#1d4a2b;
  --green-mid:#2f7a3a;
  --ink:#333;
  --muted:#888;
  --gray-bg:#f1f1f1;
  --white:#fff;
}
*{margin:0;padding:0;box-sizing:border-box}
html,body{width:1200px;height:1200px;overflow:hidden;background:var(--white);font-family:"Open Sans",sans-serif;color:var(--ink)}
.page{position:absolute;left:283px;top:0;width:634px;height:1200px;background:var(--white);overflow:hidden}
.abs{position:absolute}

/* hero */
.hero{left:0;top:0;width:634px;height:293px;background:linear-gradient(180deg,#5b5550 0%,#8c7a66 40%,#b9a58c 75%,#d8cbb7 100%)}
.topbar{left:0;top:0;width:634px;height:62px;background:rgba(40,40,40,.55);display:flex;align-items:center;padding:0 20px;justify-content:space-between}
.brand{display:flex;align-items:center;gap:6px;color:var(--white);font-weight:800;font-size:18px;letter-spacing:.5px}
.brand-dot{width:14px;height:14px;border-radius:50%;background:var(--green)}
.nav{display:flex;gap:4px;font-size:6.5px;font-weight:700;color:var(--white);text-transform:uppercase}
.nav span{padding:6px 8px}
.nav .active{background:var(--green)}
.hero-title{left:0;top:150px;width:634px;text-align:center;color:var(--white);font-style:italic;font-weight:700;font-size:22px;line-height:1.15;text-shadow:0 1px 3px rgba(0,0,0,.4)}
.hero-title em{display:block;font-size:23px}

/* section heading */
.sec-head{display:flex;align-items:center;gap:8px}
.sec-head h2{text-align:right;color:var(--green);font-weight:800;font-size:16px;line-height:1.05;text-transform:uppercase}
.sec-head h2 span{color:var(--ink);display:block}
.sec-head .bar{width:4px;height:36px;background:var(--green)}
.sec-head .mini-brand{display:flex;align-items:center;gap:4px;font-weight:800;font-size:13px;color:var(--green)}
.sec-head .mini-brand i{width:10px;height:10px;border-radius:50%;background:var(--green);display:block}
.arrows{display:flex;gap:3px}
.arrows b{width:14px;height:10px;border:1px solid #bbb;background:var(--white);display:flex;align-items:center;justify-content:center}

/* areas */
.areas{left:0;top:293px;width:634px;height:264px;background:var(--gray-bg)}
.card{position:absolute;top:79px;width:168px}
.card .photo{height:115px;width:100%}
.card h3{font-size:8px;font-weight:700;color:var(--green-mid);margin-top:15px}
.card p{font-size:5.5px;line-height:1.5;color:var(--muted);margin-top:4px}

/* portfolio */
.works{left:0;top:557px;width:634px;height:307px;background:var(--white)}
.grid{position:absolute;left:48px;top:96px;width:538px;display:grid;grid-template-columns:repeat(4,1fr);grid-template-rows:96px 96px;gap:2px}
.tile-label{display:flex;align-items:flex-end;justify-content:center;padding-bottom:10px;color:var(--white);font-size:7px;font-weight:700;text-transform:uppercase;background:var(--green)}

/* clients */
.clients{left:0;top:864px;width:634px;height:216px;background:var(--gray-bg)}
.partners{position:absolute;left:108px;top:78px;display:grid;grid-template-columns:60px 60px;row-gap:14px;column-gap:8px}
.partner{display:flex;align-items:center;gap:3px;font-size:7px;font-weight:700;color:#c23a2b}
.partner i{width:8px;height:8px;background:#c23a2b;display:block}
.partner.blue{color:#2b4f8c}.partner.blue i{background:#2b4f8c}
.testi{position:absolute;top:80px;width:124px;text-align:center}
.testi .q{width:12px;height:12px;background:var(--green-dark);margin:0 auto 6px}
.testi p{font-size:5px;line-height:1.5;color:var(--muted);background:var(--white);padding:6px}
.testi .who{font-size:5.5px;font-weight:700;color:var(--ink);margin-top:20px}
.testi .role{font-size:5px;color:var(--muted)}

/* footer */
.footer{left:0;top:1080px;width:634px;height:120px;background:var(--green-dark);color:var(--white)}
.fcol{position:absolute;top:18px;font-size:6px;line-height:1.55}
.fcol h4{font-size:6.5px;font-weight:700;text-transform:uppercase;margin-bottom:4px;display:flex;align-items:center;gap:4px}
.fcol h4 svg{width:8px;height:8px}
.f-brand{position:absolute;left:470px;top:44px;display:flex;align-items:center;gap:6px;font-weight:800;font-size:18px}
.f-brand i{width:14px;height:14px;border-radius:50%;background:var(--white);display:block}
.to-top{position:absolute;left:566px;top:42px;width:22px;height:22px;border:1.5px solid var(--white);border-radius:50%;display:flex;align-items:center;justify-content:center}
</style>
</head>
<body>
<div class="page">

  <section class="abs hero" role="img" aria-label="Foto de três engenheiros com capacetes analisando uma planta de obra"></section>
  <header class="abs topbar">
    <div class="brand"><span class="brand-dot"></span>Estrutor</div>
    <nav class="nav">
      <span class="active">Página Inicial</span><span>A Empresa</span><span>Áreas de Atuação</span><span>Portfólio</span><span>Contato</span>
    </nav>
  </header>
  <h1 class="abs hero-title">Prestamos serviços de<em>Engenharia &amp; Construção Civil</em></h1>

  <section class="abs areas">
    <div class="sec-head abs" style="left:188px;top:20px">
      <h2>Áreas<span>de atuação</span></h2><div class="bar"></div>
      <div class="mini-brand"><i></i>Estrutor</div>
    </div>
    <div class="arrows abs" style="left:560px;top:36px"><b></b><b></b></div>

    <article class="card" style="left:48px">
      <div class="photo" role="img" aria-label="Foto de engenheiros com capacetes em vistoria" style="background:linear-gradient(160deg,#e6e2da,#9c8f7d 60%,#4c4a48)"></div>
      <h3>Avaliações &amp; Perícias</h3>
      <p>Laudos técnicos e perícias para imóveis, obras e processos, com rigor e prazo garantido para cada cliente.</p>
    </article>
    <article class="card" style="left:233px">
      <div class="photo" role="img" aria-label="Foto de equipe trabalhando em obra com estrutura metálica" style="background:linear-gradient(170deg,#a9b9c4,#7f7b6c 55%,#5a4e40)"></div>
      <h3>Obras e Reformas</h3>
      <p>Execução de obras e reformas particulares com planejamento, orçamento claro e equipe experiente do início ao fim.</p>
    </article>
    <article class="card" style="left:418px">
      <div class="photo" role="img" aria-label="Foto de mãos assinando documentos de contrato" style="background:linear-gradient(160deg,#f4f4f2,#c9ccd0 55%,#6d7480)"></div>
      <h3>Licitações Públicas</h3>
      <p>Assessoria completa em licitações públicas, gerenciamento de contratos, orçamentos e planejamento de obras.</p>
    </article>
  </section>

  <section class="abs works">
    <div class="sec-head abs" style="left:210px;top:31px">
      <h2>O que<span>já fizemos</span></h2><div class="bar"></div>
      <div class="mini-brand"><i></i>Estrutor</div>
    </div>
    <div class="arrows abs" style="left:560px;top:47px"><b></b><b></b></div>
    <div class="grid">
      <div role="img" aria-label="Foto de prédio residencial junto a um lago" style="background:linear-gradient(180deg,#c9d8e4,#8aa86a 60%,#4f7a3a)"></div>
      <div role="img" aria-label="Foto de edifício comercial moderno" style="background:linear-gradient(180deg,#b7b3aa,#6f6a62)"></div>
      <div role="img" aria-label="Foto de interior de sala reformada" style="background:linear-gradient(180deg,#efe9df,#b39a7e)"></div>
      <div role="img" aria-label="Foto de casa de dois andares" style="background:linear-gradient(180deg,#dce6ee,#a8a294 60%,#6f7d5a)"></div>
      <div role="img" aria-label="Foto de prédio residencial junto a um lago, em tom verde" style="background:linear-gradient(180deg,#9ccf8a,#3f8d3c)"></div>
      <div class="tile-label" role="img" aria-label="Destaque de projeto em verde">Título do Projeto</div>
      <div role="img" aria-label="Foto de interior de sala, em tom verde" style="background:linear-gradient(180deg,#a7d597,#4e9a45)"></div>
      <div role="img" aria-label="Foto de casa de dois andares" style="background:linear-gradient(180deg,#dce6ee,#a8a294 60%,#6f7d5a)"></div>
    </div>
  </section>

  <section class="abs clients">
    <div class="sec-head abs" style="left:200px;top:12px">
      <h2>Clientes<span>&amp; parceiros</span></h2><div class="bar"></div>
      <div class="mini-brand"><i></i>Estrutor</div>
    </div>
    <div class="partners">
      <div class="partner"><i></i>Vertana</div><div class="partner"><i></i>Vertana</div>
      <div class="partner"><i></i>Obralis</div><div class="partner"><i></i>Obralis</div>
      <div class="partner blue"><i></i>Pedrix</div><div class="partner blue"><i></i>Pedrix</div>
    </div>
    <div class="testi" style="left:252px">
      <div class="q"></div>
      <p>Equipe atenciosa e técnica. A obra foi entregue no prazo e com ótimo acabamento em todos os detalhes.</p>
      <div class="who">Helena Prado</div><div class="role">Cliente</div>
    </div>
    <div class="testi" style="left:388px">
      <div class="q"></div>
      <p>Perícia detalhada e clara, que nos ajudou muito no processo. Recomendo o trabalho a todos os colegas.</p>
      <div class="who">Rafael Dias</div><div class="role">Parceiro</div>
    </div>
  </section>

  <footer class="abs footer">
    <div class="fcol" style="left:48px">
      <h4>Mapa do site</h4>
      Página Inicial<br>Quem Somos<br>Nossa História<br>Serviços<br>Política de Privacidade<br>Contato
    </div>
    <div class="fcol" style="left:178px">
      <h4><svg viewBox="0 0 10 10"><path d="M2 1l2 0 1 2-1 1a5 5 0 0 0 2 2l1-1 2 1 0 2c-4 0-7-3-7-7z" fill="#fff"/></svg>Telefones</h4>
      +55 12 98765.4310<br>+55 12 3456.7801
      <h4 style="margin-top:8px"><svg viewBox="0 0 10 10"><rect x="1" y="2" width="8" height="6" fill="#fff"/></svg>E-mail</h4>
      contato@estrutor.com.br
    </div>
    <div class="fcol" style="left:320px">
      <h4><svg viewBox="0 0 10 10"><path d="M5 9C3 6 2 5 2 4a3 3 0 0 1 6 0c0 1-1 2-3 5z" fill="#fff"/></svg>Onde estamos?</h4>
      Rua das Palmeiras, nº 128<br>Centro – Vale Verde - SP<br>CEP 11.600-000
    </div>
    <div class="f-brand"><i></i>Estrutor</div>
    <div class="to-top"><svg width="10" height="10" viewBox="0 0 10 10"><path d="M2 6l3-3 3 3" stroke="#fff" stroke-width="1.5" fill="none"/></svg></div>
  </footer>

</div>
</body>
</html>
```